Medical Cannabis company is looking for a LOGO design *

SILVER MERIDIAN (SM) is a new company in the Israeli medical cannabis industry. We will engage in PREMIUM medical cannabis growing and cultivation and also manufacturing of HIGH-END cannabis based medical products.
the design should reflect luxury, high-end and Pharma-grade products.
the design should use color GOLD and NOT using the famous cannabis leaf !

Target Market(s)

international medical cannabis Pharmaceutical companies
and of course local and international patients

Contact Information for Business Card

Ron Ben-Amit
Founder and CEO

Silver Meridian
Medical grade cannabis

ronbenamit@mailpost-example.com
972-52-3186407

Colors
ffc214
fbed22

Requirements
Must have
• clean and simple
• luxury
• gold !!
• (can also have green for Cannabis and/or blue for Pharma)
Should not have
• cannabis leaf

```html
<!DOCTYPE html>
<html lang="en">
<head>
<meta charset="utf-8">
<title>Silver Meridian — Business Card</title>
<link rel="stylesheet" href="https://fonts.googleapis.com/css2?family=Raleway:wght@600;700&display=swap">
<style>
  :root {
    --gold: #ffc214;
    --lemon: #fbed22;
    --white: #ffffff;
    --stage-light: #f7f7f7;
    --stage-dark: #6d6e70;
  }
  html, body {
    margin: 0;
    padding: 0;
    width: 1200px;
    height: 1200px;
    overflow: hidden;
  }
  .stage {
    position: relative;
    width: 1200px;
    height: 1200px;
    background: radial-gradient(circle at 600px 600px, var(--stage-light) 0%, #b9b9ba 40%, var(--stage-dark) 75%);
    font-family: "Raleway", sans-serif;
    color: var(--white);
  }
  .card {
    position: absolute;
    left: 246px;
    width: 707px;
    background: var(--lemon);
    overflow: hidden;
  }
  .card-front { top: 134px; height: 424px; }
  .card-back { top: 641px; height: 425px; }
  .card-shape {
    position: absolute;
    inset: 0;
    width: 100%;
    height: 100%;
  }
  .card-shape path { fill: var(--gold); }
  .front-text {
    position: absolute;
    left: 0;
    top: 185px;
    width: 684px;
    text-align: center;
    font-weight: 600;
    font-size: 44px;
    line-height: 59px;
    margin: 0;
  }
  .company {
    position: absolute;
    left: 0;
    top: 108px;
    width: 458px;
    text-align: center;
    font-weight: 600;
    font-size: 30px;
    line-height: 41px;
    margin: 0;
  }
  .contact {
    position: absolute;
    left: 24px;
    display: flex;
    align-items: center;
    font-weight: 600;
    font-size: 26px;
    letter-spacing: 0.3px;
  }
  .contact-email { top: 249px; }
  .contact-phone { top: 322px; }
  .contact-icon {
    width: 54px;
    height: 54px;
    margin-right: 22px;
    flex: none;
  }
  .contact-icon circle { fill: var(--white); }
  .contact-icon .glyph { fill: var(--gold); }
</style>
</head>
<body>
<div class="stage">
  <section class="card card-front">
    <svg class="card-shape" viewBox="0 0 707 424" preserveAspectRatio="none" aria-hidden="true">
      <path d="M0,424 C30,170 320,15 707,0 V424 Z"/>
    </svg>
    <p class="front-text">Ron Ben-Amit<br>Founder and CEO</p>
  </section>

  <section class="card card-back">
    <svg class="card-shape" viewBox="0 0 707 425" preserveAspectRatio="none" aria-hidden="true">
      <path d="M0,0 C360,10 645,160 661,425 H0 Z"/>
    </svg>
    <p class="company">Silver Meridian<br>Medical grade cannabis</p>

    <div class="contact contact-email">
      <svg class="contact-icon" viewBox="0 0 54 54" aria-hidden="true">
        <circle cx="27" cy="27" r="26"/>
        <path class="glyph" d="M14,21 L27,13 L40,21 V37 H14 Z"/>
        <path d="M14,21 L27,30 L40,21" fill="none" stroke="#ffffff" stroke-width="2.5"/>
      </svg>
      <span>ronbenamit@mailpost-example.com</span>
    </div>

    <div class="contact contact-phone">
      <svg class="contact-icon" viewBox="0 0 54 54" aria-hidden="true">
        <circle cx="27" cy="27" r="26"/>
        <path class="glyph" d="M19,14 C17,14 14,17 14,20 C15,30 24,39 34,40 C37,40 40,37 40,35 L35,30 L31,33 C27,31 23,27 21,23 L24,19 Z"/>
      </svg>
      <span>972-52-3186407</span>
    </div>
  </section>
</div>
</body>
</html>
```